Bright Path Flyer Design for Virtual Online Clinic. -5.5 x 8.5 inches (half sheet)

We need a clean, modern flyer design for Bright Path, a new virtual walk-in clinic based in British Columbia. The flyer will be used in libraries, pharmacies, and community centers to help residents easily access primary care through their Bright Path NFC access card.
The flyer will ask a question : NEED A DOCTOR? This should be large and attention grabbing.
The design should clearly feature a Bright Path card image (the access card) as the centerpiece and visually show how patients can use it to book appointments. The tone should feel trustworthy, healthcare-oriented, and community-friendly — clean fonts, clear spacing, and strong readability from a distance.

Side One: This card has the NFC Access Card.
NEED A DOCTOR? (Large Font, Attention Grabbing)
How to Book an Appointment using your Bright Path Card
Step 1: Tap Your Card on Your Phone
Hold your card near the back of your phone.
It will activate automatically — no app needed.
The Bright Path scheduler will open.
Step 2: Schedule Your Appointment
Select your clinical concern.
Choose your time window.
Register (only once).
Confirm your appointment.
Step 3: Relax, we’ll take care of the rest
A doctor will call during your scheduled time.
Once booked, you’ll be able to call our office.
No emails, no texts — just a real person.
It’s that simple.
Side Two:
About Bright Path
Created by Dr. Marcus Ferrigan
Bright Path was founded to make healthcare simple and convenient. Prescription renewals. Common infections. Medical notes. And so much more.
Our doctors can address 120+ health concerns virtually — providing quality care without the waiting room. No waiting rooms. Just real doctors providing real care.
Why Patients Choose Bright Path
Easy access – book and be seen from anywhere in BC.
Effortless booking – tap your Bright Path Card to begin.
Trusted physicians – every visit is with a licensed BC family doctor.
How It Works
Book your visit — choose a time window that fits your day.
Join the queue — you’ll be called when it’s your turn.
Speak directly with your doctor — simple, secure, and stress-free.
Convenient Care for Common Concerns

Additional Details.
Please find the domain to be launched soon. I've attached the NFC card file for review, it is 85.5 mm x 54 mm. The card will be glued to the flyer.
I've attached examples of flyers but they are not the look I am seeking and I am looking for creative solutions.
Thank you!
http://brightpath-example.test/

Adult Patients in British Columbia

Healthcare

• Looking for clean lines, uniform appearance, and high legibility i.e poppins

0054AA
0677BA
7BADD7
CADEEF
E8F1F8

• Need A Doctor?
• Elegant style, not too busy, clear layout.
• Clutter, look cheap - review examples.

```html
<!DOCTYPE html>
<html lang="en">
<head>
<meta charset="utf-8">
<title>Bright Path – Flyer, Front and Back</title>
<link href="https://fonts.googleapis.com/css2?family=Montserrat:ital,wght@0,400;0,500;0,600;0,700;0,800;1,700&display=swap" rel="stylesheet">
<style>
  :root {
    --navy: #27428e;
    --navy-soft: #3a55a0;
    --white: #ffffff;
    --backdrop: #e4e4e4;
    --tint: #cadeef;
    --wash: #e8f1f8;
  }
  * { box-sizing: border-box; margin: 0; padding: 0; }
  html, body { width: 1200px; height: 1200px; overflow: hidden; }
  body {
    background: var(--backdrop);
    font-family: "Montserrat", sans-serif;
    position: relative;
  }
  .flyer {
    position: absolute;
    top: 188px;
    width: 532px;
    height: 822px;
    overflow: hidden;
  }
  .flyer--front { left: 49px; background: var(--white); color: var(--navy); }
  .flyer--back { left: 618px; background: var(--navy); color: var(--white); }

  /* Brand name */
  .brand {
    position: absolute;
    font-weight: 600;
    letter-spacing: 0.02em;
    display: flex;
    align-items: center;
    gap: 8px;
  }
  .brand__dot { width: 9px; height: 9px; border-radius: 50%; background: currentColor; }
  .flyer--front .brand { left: 39px; top: 38px; font-size: 24px; }
  .flyer--back .brand { right: 50px; top: 62px; font-size: 32px; }

  /* Decorative areas */
  .decor-front {
    position: absolute; left: 345px; top: 0; width: 187px; height: 822px;
    background: linear-gradient(160deg, var(--wash) 0%, var(--tint) 100%);
  }
  .decor-back {
    position: absolute; left: 360px; top: 430px; width: 172px; height: 392px;
    background: linear-gradient(200deg, rgba(123,173,215,0.05) 0%, rgba(123,173,215,0.3) 100%);
  }

  /* Front headline */
  .headline {
    position: absolute; left: 42px; top: 132px;
    font-weight: 800; line-height: 1;
  }
  .headline__big { display: block; font-size: 76px; letter-spacing: 0.01em; }
  .headline__small { display: block; font-size: 46px; margin-top: 8px; }

  .booking-title {
    position: absolute; left: 42px; top: 402px;
    font-size: 18px; font-weight: 700; font-style: italic; line-height: 1.18;
  }

  /* Steps */
  .step { position: absolute; left: 0; width: 345px; }
  .step--one { top: 481px; height: 96px; }
  .step--two { top: 577px; height: 125px; width: 326px; background: var(--navy); color: var(--white); }
  .step--three { top: 702px; height: 120px; }
  .step__tab {
    position: absolute; left: 34px; top: 0; bottom: 0; width: 23px;
    background: var(--navy); color: var(--white);
    display: flex; align-items: center; justify-content: center;
  }
  .step__tab span {
    transform: rotate(-90deg); white-space: nowrap;
    font-size: 13px; font-weight: 700; letter-spacing: 0.04em;
  }
  .step__body { position: absolute; left: 70px; top: 10px; right: 8px; }
  .step__title { font-size: 11.5px; font-weight: 700; margin-bottom: 10px; }
  .step__text { font-size: 11px; font-weight: 500; line-height: 1.4; }
  .step__text + .step__text { margin-top: 9px; }

  /* Back content */
  .about { position: absolute; left: 34px; top: 176px; width: 470px; }
  .about__title { font-size: 27px; font-weight: 700; line-height: 1.1; }
  .about__byline { font-size: 14.5px; font-weight: 700; font-style: italic; margin-top: 2px; }
  .about__para { font-size: 13px; font-weight: 400; line-height: 1.35; margin-top: 20px; }
  .about__para + .about__para { margin-top: 18px; }
  .section-title { font-size: 17px; font-weight: 700; margin-top: 20px; margin-bottom: 3px; }
  .ticks { list-style: none; }
  .ticks li {
    font-size: 13px; line-height: 1.3; display: flex; align-items: flex-start; gap: 5px;
  }
  .ticks svg { flex: none; width: 10px; height: 10px; margin-top: 4px; }
</style>
</head>
<body>

<section class="flyer flyer--front">
  <div class="decor-front" role="img" aria-label="Large outlined bird brand decoration"></div>

  <div class="brand"><span class="brand__dot"></span>Bright Path</div>

  <h1 class="headline">
    <span class="headline__big">NEED</span>
    <span class="headline__small">A DOCTOR?</span>
  </h1>

  <p class="booking-title">How to Book<br>an Appointment using<br>your Bright Path Card</p>

  <div class="step step--one">
    <div class="step__tab"><span>STEP 1</span></div>
    <div class="step__body">
      <p class="step__title">Tap Your Card on Your Phone</p>
      <p class="step__text">Hold your card near the back of your phone.</p>
      <p class="step__text">It will activate automatically — no app needed.<br>The Bright Path scheduler will open.</p>
    </div>
  </div>

  <div class="step step--two">
    <div class="step__tab"><span>STEP 2</span></div>
    <div class="step__body">
      <p class="step__title">Schedule Your Appointment</p>
      <p class="step__text">Select your clinical concern.<br>Choose your time window.</p>
      <p class="step__text">Register (only once).<br>Confirm your appointment.</p>
    </div>
  </div>

  <div class="step step--three">
    <div class="step__tab"><span>STEP 3</span></div>
    <div class="step__body">
      <p class="step__title">Relax, we’ll take care of the rest</p>
      <p class="step__text">A doctor will call during your scheduled time.<br>Once booked, you’ll be able to call our office.<br>No emails, no texts — just a real person.<br>It’s that simple.</p>
    </div>
  </div>
</section>

<section class="flyer flyer--back">
  <div class="decor-back" role="img" aria-label="Faint bird brand decoration"></div>

  <div class="brand"><span class="brand__dot"></span>Bright Path</div>

  <div class="about">
    <h2 class="about__title">About Bright Path</h2>
    <p class="about__byline">Created by Dr. Marcus Ferrigan</p>
    <p class="about__para">Bright Path was founded to make healthcare simple and convenient. Prescription renewals. Common infections. Medical notes. And so much more.</p>
    <p class="about__para">Our doctors can address 120+ health concerns virtually — providing quality care without the waiting room. No waiting rooms. Just real doctors providing real care.</p>

    <h3 class="section-title">Why Patients Choose Bright Path</h3>
    <ul class="ticks">
      <li><svg viewBox="0 0 10 10"><path d="M1 5.5 L4 8.5 L9 1.5" fill="none" stroke="currentColor" stroke-width="1.6"/></svg>Easy access – book and be seen from anywhere in BC.</li>
      <li><svg viewBox="0 0 10 10"><path d="M1 5.5 L4 8.5 L9 1.5" fill="none" stroke="currentColor" stroke-width="1.6"/></svg>Effortless booking – tap your Bright Path Card to begin.</li>
      <li><svg viewBox="0 0 10 10"><path d="M1 5.5 L4 8.5 L9 1.5" fill="none" stroke="currentColor" stroke-width="1.6"/></svg>Trusted physicians – every visit is with a licensed BC family doctor.</li>
    </ul>

    <h3 class="section-title">How It Works</h3>
    <ul class="ticks">
      <li><svg viewBox="0 0 10 10"><path d="M1 5.5 L4 8.5 L9 1.5" fill="none" stroke="currentColor" stroke-width="1.6"/></svg>Book your visit — choose a time window that fits your day.</li>
      <li><svg viewBox="0 0 10 10"><path d="M1 5.5 L4 8.5 L9 1.5" fill="none" stroke="currentColor" stroke-width="1.6"/></svg>Join the queue — you’ll be called when it’s your turn.</li>
      <li><svg viewBox="0 0 10 10"><path d="M1 5.5 L4 8.5 L9 1.5" fill="none" stroke="currentColor" stroke-width="1.6"/></svg>Speak directly with your doctor — simple, secure, and stress-free.</li>
      <li><svg viewBox="0 0 10 10"><path d="M1 5.5 L4 8.5 L9 1.5" fill="none" stroke="currentColor" stroke-width="1.6"/></svg>Convenient Care for Common Concerns</li>
    </ul>
  </div>
</section>

</body>
</html>
```